We are a music event management company based out of Syracuse, NY but we do business in multiple areas like the mid-west and Florida.

Our primary events revolve around the Electronic Dance Music scene. (acts like Brinmoor, Nordic Loft Syndicate, Dorian Pell)

We would like a clean cut business card with Voltaramble written on the back. In Voltaramble we would like the u to be shaped like a sixteenth note. The colors green and silver would be nice to see somehow but not necessary. Feel free to play around with it and have fun because that's what our business is about, Having Fun!

Some similar examples for reference would be the Neon Orchard or Glowing Tulip Jamboree website.

Our goal is to provide people with an experience, not just a concert. There is a difference.

Reason: Needed more time to decide.

Industry/Entity Type

Events

```html
<!DOCTYPE html>
<html lang="en">
<head>
<meta charset="utf-8">
<title>Voltaramble Business Card</title>
<link href="https://fonts.googleapis.com/css2?family=Raleway:wght@300;400&display=swap" rel="stylesheet">
<style>
  :root {
    --backdrop: #4a4a4a;
    --card: #ffffff;
    --ink: #2b2b2b;
    --ink-soft: #444444;
    --icon: #a8a8a8;
    --accent-pink: #f2337c;
    --eq-dark: #0f2a1c;
    --eq-green: #2fae5a;
    --eq-light: #9be0a8;
    --eq-teal: #1f8f86;
  }
  * { box-sizing: border-box; margin: 0; padding: 0; }
  html, body {
    width: 1200px; height: 1000px; overflow: hidden;
    background: var(--backdrop);
    font-family: "Raleway", sans-serif;
    font-weight: 300;
  }
  .stage { position: relative; width: 1200px; height: 1000px; }
  .card {
    position: absolute; left: 250px; width: 700px; height: 438px;
    background: var(--card); overflow: hidden;
  }
  .card--front { top: 46px; }
  .card--back { top: 516px; }

  .equalizer-art {
    position: absolute; left: 25px; top: 65px; width: 640px; height: 290px;
    background:
      radial-gradient(ellipse 55% 22% at 50% 50%, rgba(31,143,134,0.85), rgba(31,143,134,0) 100%),
      linear-gradient(180deg,
        rgba(155,224,168,0) 0%,
        rgba(155,224,168,0.55) 18%,
        var(--eq-green) 36%,
        var(--eq-dark) 50%,
        var(--eq-green) 64%,
        rgba(155,224,168,0.55) 82%,
        rgba(155,224,168,0) 100%);
    -webkit-mask-image: linear-gradient(90deg, transparent 0%, #000 6%, #000 94%, transparent 100%);
            mask-image: linear-gradient(90deg, transparent 0%, #000 6%, #000 94%, transparent 100%);
  }

  .contact {
    position: absolute; display: flex; align-items: center; gap: 5px;
    font-size: 19px; font-weight: 300; color: var(--ink); white-space: nowrap;
  }
  .contact svg { fill: var(--icon); flex: none; }
  .contact--address { left: 86px; top: 66px; }
  .contact--phone { left: 90px; top: 352px; }
  .contact--email { left: 387px; top: 366px; }

  .holder-name {
    position: absolute; left: 55px; top: 193px;
    font-size: 44px; font-weight: 300; color: #ffffff;
    white-space: nowrap; letter-spacing: 0.3px;
  }
  .holder-role { color: var(--accent-pink); margin-left: 12px; font-weight: 300; }

  .brand-strip {
    position: absolute; top: 207px; height: 32px;
    background: linear-gradient(90deg, var(--eq-dark), var(--eq-green) 55%, var(--eq-light));
  }
  .brand-strip--left { left: 0; width: 112px; }
  .brand-strip--right { left: 645px; width: 55px;
    background: linear-gradient(90deg, var(--eq-light), var(--eq-green) 45%, var(--eq-dark)); }

  .brand-line {
    position: absolute; left: 126px; top: 192px;
    display: flex; align-items: baseline; gap: 10px; white-space: nowrap;
  }
  .brand-name { font-size: 45px; font-weight: 300; color: var(--ink); }
  .brand-web { font-size: 22px; font-weight: 300; color: var(--ink-soft); }
</style>
</head>
<body>
<main class="stage">
  <section class="card card--front">
    <div class="equalizer-art" role="img" aria-label="Green audio equalizer bars mirrored around a central band"></div>

    <p class="contact contact--address">
      <svg width="14" height="20" viewBox="0 0 14 20" aria-hidden="true"><path d="M7 0C3.1 0 0 3.1 0 7c0 5 7 13 7 13s7-8 7-13c0-3.9-3.1-7-7-7zm0 9.5A2.5 2.5 0 1 1 7 4.5a2.5 2.5 0 0 1 0 5z"/></svg>
      PO Box 418 | Larkspur Hollow | KT 40118
    </p>

    <h1 class="holder-name">Colin R Vandermeer<span class="holder-role">CEO</span></h1>

    <p class="contact contact--phone">
      <svg width="14" height="20" viewBox="0 0 14 20" aria-hidden="true"><path d="M3 1l3 0 1 5-2 1.5c.8 2.5 2 4.5 3.8 6L11 12l3 3-1 3.5c-6-1-11-8-11-14.5z"/></svg>
      555 014 2837
    </p>

    <p class="contact contact--email">
      <svg width="18" height="13" viewBox="0 0 18 13" aria-hidden="true"><path d="M0 0h18v13H0z" fill="var(--icon)"/><path d="M1.5 1.5L9 7l7.5-5.5" fill="none" stroke="#fff" stroke-width="1.4"/></svg>
      colin@voltaramblekt.com
    </p>
  </section>

  <section class="card card--back">
    <div class="brand-strip brand-strip--left" role="img" aria-label="Green equalizer bar strip"></div>
    <div class="brand-line">
      <span class="brand-name">Voltaramble</span>
      <span class="brand-web">www.voltaramblekt.com</span>
    </div>
    <div class="brand-strip brand-strip--right" role="img" aria-label="Green equalizer bar strip"></div>
  </section>
</main>
</body>
</html>
```